A Maple Syrup Label for a Local Buniness

We are looking for a label for our maple syrup business. Our business currently sells honey, and we are expanding into maple syrup. Our Business name is "Corvale Bees" and we currently have a logo attached below. We would like to incorporate the bee and CB part, but the label could also read "Corvale Farms" with the words maple syrup. We do not want consumers to confuse the maple syrup jars with the honey jars. It should be clear that the jars contain maple syrup. We are open to new designs as well.

```html
<!DOCTYPE html>
<html lang="en">
<head>
<meta charset="utf-8">
<title>Maple Syrup Label – Corvale Farms</title>
<link href="https://fonts.googleapis.com/css2?family=Oswald:wght@600;700&family=Cinzel:wght@500&family=Roboto:wght@700&display=swap" rel="stylesheet">
<style>
  :root {
    --paper: #e6d3b0;
    --paper-light: #ecdcbc;
    --drip-dark: #e8641a;
    --drip-light: #f7b53a;
    --maple-red: #b9172a;
    --syrup-orange: #e5501e;
    --badge-green: #14923a;
    --brand-black: #1c1c1c;
    --brand-gold: #f2b705;
    --size-brown: #5b3312;
    --band-text: #ecd9b5;
  }
  html, body { margin: 0; padding: 0; overflow: hidden; }
  .label {
    position: relative;
    width: 800px;
    height: 1200px;
    overflow: hidden;
    background: var(--paper);
  }
  .paper-wash {
    position: absolute;
    left: 40px; top: 90px; right: 40px; bottom: 60px;
    background: var(--paper-light);
    border-radius: 30px;
  }
  .drip-band {
    position: absolute;
    left: 0; top: 0;
    width: 800px; height: 80px;
    background: linear-gradient(180deg, var(--drip-dark), var(--drip-light) 70%, var(--drip-dark));
  }
  .brand-mark {
    position: absolute;
    left: 0; top: 120px;
    width: 800px;
    display: flex;
    justify-content: center;
    align-items: center;
    gap: 14px;
  }
  .brand-mark .dot {
    width: 34px; height: 34px;
    border-radius: 50%;
    background: var(--brand-gold);
  }
  .brand-mark .name {
    font-family: "Oswald", sans-serif;
    font-weight: 600;
    font-size: 48px;
    color: var(--brand-black);
    letter-spacing: 2px;
  }
  .badge {
    position: absolute;
    top: 276px;
    width: 130px;
    text-align: center;
  }
  .badge--natural { left: 54px; }
  .badge--vegetarian { left: 616px; }
  .badge svg { display: block; margin: 0 auto; }
  .badge .caption {
    margin-top: 8px;
    font-family: "Roboto", sans-serif;
    font-weight: 700;
    font-size: 12px;
    color: var(--badge-green);
    white-space: nowrap;
  }
  .title {
    position: absolute;
    left: 0; width: 800px;
    margin: 0;
    text-align: center;
    font-family: "Oswald", sans-serif;
    font-weight: 700;
    line-height: 1;
  }
  .title--maple {
    top: 432px;
    font-size: 200px;
    color: var(--maple-red);
    letter-spacing: 2px;
  }
  .title--syrup {
    top: 638px;
    font-size: 200px;
    color: var(--syrup-orange);
    letter-spacing: 2px;
  }
  .maple-leaf {
    position: absolute;
    left: 560px; top: 632px;
    width: 108px; height: 108px;
    border-radius: 50% 10% 50% 10%;
    background: linear-gradient(135deg, #e0452b, #8e1414);
    transform: rotate(-10deg);
  }
  .farm-band {
    position: absolute;
    left: 91px; top: 925px;
    width: 617px; height: 70px;
    border-radius: 35px;
    background: var(--syrup-orange);
    display: flex;
    align-items: center;
    justify-content: center;
    font-family: "Cinzel", serif;
    font-weight: 500;
    font-size: 40px;
    letter-spacing: 8px;
    color: var(--band-text);
  }
  .net-weight {
    position: absolute;
    left: 0; top: 1045px;
    width: 800px;
    text-align: center;
    font-family: "Oswald", sans-serif;
    font-weight: 600;
    font-size: 44px;
    color: var(--size-brown);
  }
</style>
</head>
<body>
<div class="label">
  <div class="paper-wash"></div>
  <div class="drip-band" role="img" aria-label="Golden syrup dripping along the top edge"></div>

  <div class="brand-mark">
    <span class="dot"></span>
    <span class="name">Corvale Bees</span>
  </div>

  <div class="badge badge--natural">
    <svg width="118" height="118" viewBox="0 0 118 118" aria-hidden="true">
      <circle cx="59" cy="59" r="55" fill="none" stroke="var(--badge-green)" stroke-width="5"/>
    </svg>
    <div class="caption">100% NATURAL</div>
  </div>

  <div class="badge badge--vegetarian">
    <svg width="118" height="118" viewBox="0 0 118 118" aria-hidden="true">
      <circle cx="59" cy="59" r="55" fill="none" stroke="var(--badge-green)" stroke-width="5"/>
    </svg>
    <div class="caption">100% VEGETARIAN</div>
  </div>

  <h1 class="title title--maple">MAPLE</h1>
  <h2 class="title title--syrup">SYRUP</h2>
  <div class="maple-leaf" role="img" aria-label="Red autumn maple leaf"></div>

  <div class="farm-band">Corvale Farms</div>

  <div class="net-weight">12 Oz</div>
</div>
</body>
</html>
```